letterhead design for a investing company*

Design an appealing business letterhead to match with our existing logo and attract new customers. Our customers are mainly corporate managers which are detail oriented and judge the company ability to perform a good service based on small details. A professional letterhead will give a good first impression.

Target Market(s)

New customers and business owners

Industry/Entity Type

Marketplace

Font styles to use
Sans Serif
Script

Requirements
Must have
• Must be a professional and elegant design that attracts interest from people who receives it

```html
<!DOCTYPE html>
<html lang="en">
<head>
<meta charset="utf-8">
<title>BrightVale Letterhead</title>
<link href="https://fonts.googleapis.com/css2?family=Lato:wght@400;700&display=swap" rel="stylesheet">
<style>
  :root {
    --backdrop: #d6d6d6;
    --paper: #ffffff;
    --gold: #fdbd12;
    --navy: #101d3d;
    --text-grey: #5d5f66;
    --ghost: #e8e9ed;
    --ghost-fade: rgba(232, 233, 237, 0);
  }
  * { margin: 0; padding: 0; box-sizing: border-box; }
  html, body {
    width: 1056px; height: 1200px; overflow: hidden;
    background: var(--backdrop);
    font-family: 'Lato', sans-serif;
  }
  .letterhead {
    position: absolute; left: 132px; top: 40px;
    width: 792px; height: 1120px;
    background: var(--paper);
    overflow: hidden;
  }
  .side-band { position: absolute; left: 0; top: 0; width: 39px; height: 1120px; }
  .brand {
    position: absolute; left: 86px; top: 96px;
    display: flex; align-items: center; gap: 14px;
  }
  .brand-dot { width: 40px; height: 40px; border-radius: 50%; background: var(--gold); }
  .brand-name {
    font-family: 'Lato', sans-serif; font-weight: 700;
    font-size: 56px; line-height: 1; color: var(--navy); letter-spacing: -0.5px;
  }
  .mascot-area {
    position: absolute; left: 350px; top: 600px; width: 500px; height: 600px;
    background: radial-gradient(ellipse closest-side at 50% 50%,
      var(--ghost) 0%, var(--ghost) 45%, var(--ghost-fade) 100%);
  }
  .contact-rail {
    position: absolute; left: 21px; top: 947px; width: 31px; height: 142px;
    background: var(--navy);
    border: 3px solid var(--paper); border-right: none;
  }
  .contact-icon { position: absolute; left: 6px; width: 16px; height: 16px; }
  .contact-lines {
    position: absolute; left: 60px; top: 959px;
    color: var(--text-grey); font-size: 16px; line-height: 19.5px;
  }
  .contact-lines p { margin: 0; }
  .contact-gap { height: 19px; }
</style>
</head>
<body>
  <div class="letterhead">
    <svg class="side-band" viewBox="0 0 39 1120" aria-hidden="true">
      <polygon points="0,0 39,0 39,298 0,276" fill="var(--gold)"/>
      <polygon points="0,287 39,308 39,1120 0,1120" fill="var(--navy)"/>
    </svg>

    <div class="brand">
      <span class="brand-dot"></span>
      <span class="brand-name">BrightVale</span>
    </div>

    <div class="mascot-area" role="img" aria-label="Faint watermark illustration of the brand mascot giving a thumbs up"></div>

    <div class="contact-rail">
      <svg class="contact-icon" style="top:15px" viewBox="0 0 16 16" aria-hidden="true">
        <path d="M8 1a5 5 0 0 0-5 5c0 4 5 9 5 9s5-5 5-9a5 5 0 0 0-5-5zm0 7a2 2 0 1 1 0-4 2 2 0 0 1 0 4z" fill="#fff"/>
      </svg>
      <svg class="contact-icon" style="top:73px" viewBox="0 0 16 16" aria-hidden="true">
        <path d="M4 2l2.5 3-1.5 1.5c.8 1.8 2.2 3.2 4 4l1.5-1.5 3 2.5-1.5 2C7 13 3 9 2 4z" fill="none" stroke="#fff" stroke-width="1.5" stroke-linejoin="round"/>
      </svg>
      <svg class="contact-icon" style="top:94px" viewBox="0 0 16 16" aria-hidden="true">
        <rect x="1.5" y="3.5" width="13" height="9" fill="none" stroke="#fff" stroke-width="1.3"/>
        <path d="M1.5 3.5 8 9l6.5-5.5" fill="none" stroke="#fff" stroke-width="1.3"/>
      </svg>
      <svg class="contact-icon" style="top:116px" viewBox="0 0 16 16" aria-hidden="true">
        <circle cx="8" cy="8" r="6.3" fill="none" stroke="#fff" stroke-width="1.2"/>
        <ellipse cx="8" cy="8" rx="2.8" ry="6.3" fill="none" stroke="#fff" stroke-width="1"/>
        <path d="M1.7 8h12.6M2.6 5h10.8M2.6 11h10.8" stroke="#fff" stroke-width="1"/>
      </svg>
    </div>

    <div class="contact-lines">
      <p>1234 First Line Address</p>
      <p>5678 Second Line Address</p>
      <div class="contact-gap"></div>
      <p>(111) 999-0000</p>
      <p>Info@yourmail.com</p>
      <p>www.yourwebsite.com</p>
    </div>
  </div>
</body>
</html>
```